The name of the company is Kestrel Rehab buying foreclosed homes and remodeling

A sleek classy card. It’s a home remodel and house flip company. Something mostly black with dark gray and red in color . Something with two f”s as a logo on front as shown in pictures. Kind of just let you guys run with it . I left a few pictures that should help
You guys get an idea of what I thought was good also left all the information for back of the card

Target Market(s)

Home remodel consumers

Industry/Entity Type

Construction Company

Contact Information for Business Card

All details are on photo

Font styles to use
Decorative

Colors

Designer to choose colors to be used in the design.

Requirements
Must have
• Name of company on front. Kestrel Rehab
Nice to have
• Up to you guys I trust you
Should not have
• Not sure

```html
<!DOCTYPE html>
<html lang="en">
<head>
<meta charset="UTF-8">
<title>Kestrel Rehab — Business Card</title>
<link href="https://fonts.googleapis.com/css2?family=Audiowide&family=Roboto:wght@400;700&display=swap" rel="stylesheet">
<style>
  :root{
    --page:#2a2a2d;
    --card-black:#0d0d0e;
    --card-gray:#1c1c1e;
    --red:#e8242b;
    --red-mid:#d21f26;
    --red-dark:#b81b21;
    --white:#ffffff;
    --light-gray:#d4d4d4;
  }
  *{box-sizing:border-box;margin:0;padding:0}
  html,body{width:1200px;height:800px;overflow:hidden;background:var(--page)}
  .canvas{width:1200px;height:800px;display:flex;flex-direction:column;align-items:center;justify-content:center;gap:36px}
  .card{position:relative;width:600px;height:343px;background:var(--card-black);overflow:hidden;box-shadow:0 14px 30px rgba(0,0,0,.45)}
  .card__photo{position:absolute;inset:0;background:linear-gradient(160deg,#1f1f21 0%,#121213 55%,#0a0a0a 100%)}
  .brand{position:relative;display:flex;align-items:center;gap:12px}
  .brand__mark{width:16px;height:16px;background:var(--red)}
  .brand__name{font-family:"Audiowide",sans-serif;color:var(--white);font-size:36px;letter-spacing:1px}

  /* front */
  .card--front .brand{position:absolute;left:0;right:0;top:118px;justify-content:center}
  .tagline{position:absolute;left:0;right:0;bottom:44px;text-align:center;font-family:"Roboto",sans-serif;font-weight:700;font-size:13.5px;color:var(--white);letter-spacing:.3px}

  /* back */
  .card--back .brand{position:absolute;left:30px;top:140px}
  .card--back .brand__name{font-size:26px}
  .website{position:absolute;left:60px;bottom:26px;font-family:"Roboto",sans-serif;font-weight:700;font-size:14px;color:var(--white)}
  .contact{position:absolute;right:0;top:0;width:318px;height:272px;display:flex;flex-direction:column}
  .contact__row{flex:1;display:flex;align-items:center;background:var(--red)}
  .contact__row:nth-child(odd){background:var(--red-mid)}
  .contact__icon{width:62px;height:100%;display:flex;align-items:center;justify-content:center;background:var(--red-dark)}
  .contact__icon svg{width:24px;height:24px;fill:none;stroke:var(--white);stroke-width:1.6;stroke-linecap:round;stroke-linejoin:round}
  .contact__text{padding-left:22px;font-family:"Roboto",sans-serif;font-weight:700;font-size:14px;color:var(--white)}
  .contact__name{font-size:16px;display:block}
  .contact__role{display:block;font-weight:400;font-size:9px;letter-spacing:2px;margin-top:3px}
</style>
</head>
<body>
<main class="canvas">
  <section class="card card--front">
    <div class="card__photo" role="img" aria-label="Dark photo of a renovated two-storey house"></div>
    <div class="brand"><span class="brand__mark"></span><span class="brand__name">Kestrel Rehab</span></div>
    <p class="tagline">Central Contractor | Home | Remodel | Concrete Alternatives</p>
  </section>

  <section class="card card--back">
    <div class="card__photo" role="img" aria-label="Dark photo of a renovated two-storey house"></div>
    <div class="brand"><span class="brand__mark"></span><span class="brand__name">Kestrel Rehab</span></div>
    <p class="website">www.kestrelrehab.com</p>

    <div class="contact">
      <div class="contact__row">
        <div class="contact__icon"><svg viewBox="0 0 24 24"><circle cx="12" cy="8" r="4"/><path d="M4 21c0-4 3.6-7 8-7s8 3 8 7z"/></svg></div>
        <div class="contact__text"><span class="contact__name">Daniel Whitcombe JR</span><span class="contact__role">FOUNDER / OWNER</span></div>
      </div>
      <div class="contact__row">
        <div class="contact__icon"><svg viewBox="0 0 24 24"><path d="M5 4h4l2 5-2.5 1.5a11 11 0 0 0 5 5L15 13l5 2v4a2 2 0 0 1-2 2A16 16 0 0 1 3 6a2 2 0 0 1 2-2z"/></svg></div>
        <div class="contact__text">9101-555-0142</div>
      </div>
      <div class="contact__row">
        <div class="contact__icon"><svg viewBox="0 0 24 24"><rect x="3" y="6" width="18" height="13" rx="1"/><path d="M3 7l9 7 9-7"/></svg></div>
        <div class="contact__text">dwhitcombejr@mailbox.com</div>
      </div>
      <div class="contact__row">
        <div class="contact__icon"><svg viewBox="0 0 24 24"><rect x="5" y="5" width="14" height="14"/></svg></div>
        <div class="contact__text">Kestrel_Rehab_</div>
      </div>
    </div>
  </section>
</main>
</body>
</html>
```